Yard signs to bring awareness to the neighborhood we are here to help you also.

My project is to build brand awareness in a Neighborhood before during and after my company's get a home owner approve from there in insurance Approved to replace there roof due to the recent storms. Call us we can do the same for you.
We are trying to let the neighborhood know that they may also have enough storm damage for them to have there roof and gutters replace at no cost to them. And we can help with there claim to go over all the steps involved.

Target Market(s)

Brand awareness to Home owner in the neighborhood

Industry/Entity Type

Roofing

Font styles to use
Sans Serif

Requirements
Must have
• Insurance Approved
Wind & Hail
Call For Free consultation
512 846-2971
Nice to have
• Make phone # big and bold

```html
<!DOCTYPE html>
<html lang="en">
<head>
<meta charset="utf-8">
<title>J&amp;R Roofing LLC. – Yard Sign</title>
<link rel="stylesheet" href="https://fonts.googleapis.com/css2?family=Anton&family=Oswald:wght@500;600;700&display=swap">
<style>
  :root {
    --teal: #00b6a0;
    --ink: #14141a;
    --mint: #7ff5dc;
    --white: #ffffff;
    --page: #ececec;
  }
  html, body {
    margin: 0;
    padding: 0;
    width: 816px;
    height: 1200px;
    overflow: hidden;
    background: var(--page);
  }
  .canvas {
    position: relative;
    width: 816px;
    height: 1200px;
  }
  .yard-sign {
    position: absolute;
    left: 20px;
    top: 309px;
    width: 776px;
    height: 582px;
    overflow: hidden;
  }
  .sign-shapes {
    position: absolute;
    inset: 0;
    width: 100%;
    height: 100%;
  }
  .headline {
    position: absolute;
    left: 60px;
    top: 22px;
    margin: 0;
    font-family: "Oswald", sans-serif;
    font-weight: 700;
    font-size: 77px;
    line-height: 84px;
    color: var(--white);
    text-transform: uppercase;
  }
  .brand {
    position: absolute;
    left: 466px;
    top: 86px;
    width: 300px;
    height: 130px;
  }
  .brand-name {
    margin: 0 0 0 14px;
    font-family: "Oswald", sans-serif;
    font-weight: 500;
    font-size: 38px;
    line-height: 46px;
    color: var(--mint);
    letter-spacing: -0.5px;
    white-space: nowrap;
  }
  .brand-mark {
    position: absolute;
    left: 0;
    top: 62px;
    width: 42px;
    height: 42px;
    background: var(--teal);
  }
  .brand-tagline {
    position: absolute;
    left: 52px;
    top: 60px;
    width: 232px;
    margin: 0;
    font-family: "Oswald", sans-serif;
    font-weight: 500;
    font-size: 18px;
    line-height: 24px;
    color: var(--mint);
    text-align: center;
  }
  .storm-type {
    position: absolute;
    left: 58px;
    top: 228px;
    margin: 0;
    font-family: "Anton", sans-serif;
    font-weight: 400;
    font-size: 132px;
    line-height: 150px;
    color: var(--white);
    letter-spacing: 6px;
    white-space: nowrap;
  }
  .cta-pill {
    position: absolute;
    left: 307px;
    top: 420px;
    width: 445px;
    height: 48px;
    border-radius: 24px;
    background: var(--white);
    font-family: "Oswald", sans-serif;
    font-weight: 600;
    font-size: 31px;
    line-height: 48px;
    text-align: center;
    color: var(--ink);
    text-transform: uppercase;
  }
  .cta-pill .accent { color: var(--teal); }
  .phone {
    position: absolute;
    left: 305px;
    top: 474px;
    display: flex;
    align-items: center;
    gap: 12px;
  }
  .phone-icon {
    width: 52px;
    height: 52px;
    flex: none;
  }
  .phone-number {
    font-family: "Oswald", sans-serif;
    font-weight: 600;
    font-size: 68px;
    line-height: 76px;
    color: var(--white);
    letter-spacing: 1px;
  }
</style>
</head>
<body>
<main class="canvas">
  <section class="yard-sign">
    <svg class="sign-shapes" viewBox="0 0 1089 817" preserveAspectRatio="none" aria-hidden="true">
      <rect width="1089" height="817" fill="var(--teal)"/>
      <polygon fill="var(--ink)" points="0,298 569,298 697,82 1089,82 1089,545 484,545 316,749 0,749"/>
    </svg>

    <h1 class="headline">Insurance<br>Approved</h1>

    <div class="brand">
      <p class="brand-name">J&amp;R ROOFING LLC.</p>
      <span class="brand-mark"></span>
      <p class="brand-tagline">Storm Ready Roofs!<br>Here To Help.</p>
    </div>

    <h2 class="storm-type">WIND &amp; HAIL</h2>

    <div class="cta-pill">Call for <span class="accent">Free Consultation</span></div>

    <div class="phone">
      <svg class="phone-icon" viewBox="0 0 52 52" aria-hidden="true">
        <circle cx="26" cy="26" r="26" fill="var(--white)"/>
        <path d="M19 15c1.5-1 3-0.5 3.8 1l2 3.6c0.6 1.2 0.2 2.4-0.8 3.2l-1.4 1c1 2.6 3 4.6 5.6 5.6l1-1.4c0.8-1 2-1.4 3.2-0.8l3.6 2c1.5 0.8 2 2.3 1 3.8l-1.2 1.6c-1 1.3-2.8 1.9-4.4 1.4C24 33.6 18.4 28 16 20.6c-0.5-1.6 0.1-3.4 1.4-4.4z" fill="var(--ink)"/>
        <path d="M29 14a10 10 0 0 1 9 9M28.5 18.5a5.5 5.5 0 0 1 5 5" fill="none" stroke="var(--ink)" stroke-width="2.2" stroke-linecap="round"/>
      </svg>
      <span class="phone-number">512 846-2971</span>
    </div>
  </section>
</main>
</body>
</html>
```